Looking for Classic Automotive Magazine Style Covers with emphasis on American Classic Cars, Car Brand, Automotive Products, Muscle Cars and Trucks.

The Final Graphics will be used for printing large scale Wall Art for Automotive Style Man Caves, used primarily to store and showcase Classic and American Muscle Cars.

4 individual Magazine Style covers are required, with titles such as Hauler Yard, Chrome Ember, Gear Haven and Rod Servicing etc.... .Final Media to be used for digital printing with final size at 1200mm wide by 3000mm high.

The type and style needed has been attached, but happy to consider any interesting idea provided.

Additionally 1xImage required for a final print size 3000mm x 3000mm.

```html
<!DOCTYPE html>
<html lang="en">
<head>
<meta charset="utf-8">
<title>Chrome Ember — Service &amp; Repair</title>
<link rel="stylesheet" href="https://fonts.googleapis.com/css2?family=Audiowide&family=Roboto+Condensed:ital,wght@1,700;1,800&display=swap">
<style>
  :root {
    --cream-top: #f6d3b2;
    --cream-bottom: #fbeee1;
    --brick: #a61e22;
    --mustard: #ebbd3a;
    --ink: #111111;
    --navy: #1f2238;
    --white: #ffffff;
    --cream-car: #ece4d4;
    --brown-car: #4a1f16;
  }
  * { margin: 0; padding: 0; box-sizing: border-box; }
  html, body { width: 904px; height: 1200px; overflow: hidden; background: var(--white); }
  .cover {
    position: relative;
    width: 904px;
    height: 1200px;
    overflow: hidden;
    background: linear-gradient(180deg, var(--cream-top) 0%, var(--cream-bottom) 55%, var(--cream-bottom) 100%);
  }
  .backdrop { position: absolute; inset: 0; }
  .est {
    position: absolute;
    top: 50px;
    font-family: "Audiowide", sans-serif;
    font-size: 16px;
    color: var(--navy);
    letter-spacing: 1px;
  }
  .est--label { left: 140px; }
  .est--year { left: 764px; }
  .masthead {
    position: absolute;
    font-family: "Audiowide", sans-serif;
    color: var(--brick);
    line-height: 1;
    letter-spacing: -2px;
  }
  .masthead--first { left: 132px; top: 78px; font-size: 132px; }
  .masthead--second { right: 74px; top: 240px; font-size: 132px; }
  .flags {
    position: absolute;
    left: 170px; top: 236px;
    width: 120px; height: 86px;
    background: linear-gradient(135deg, #222 0%, #777 50%, #222 100%);
    opacity: .85;
  }
  .burst { position: absolute; left: 18px; top: 278px; width: 260px; height: 250px; }
  .burst-text {
    position: absolute;
    left: 28px; top: 355px;
    width: 240px;
    text-align: center;
    font-family: "Audiowide", sans-serif;
    color: var(--white);
    font-size: 26px;
    line-height: 31px;
    letter-spacing: 1px;
  }
  .ribbon { position: absolute; left: 40px; top: 410px; width: 820px; height: 170px; }
  .ribbon-text {
    position: absolute;
    left: 205px; top: 488px;
    font-family: "Audiowide", sans-serif;
    font-size: 29px;
    color: var(--white);
    letter-spacing: 3px;
    transform: rotate(-10.5deg);
    transform-origin: left bottom;
    white-space: nowrap;
    text-shadow: 2px 2px 0 var(--ink);
  }
  .tagline {
    position: absolute;
    right: 676px; top: 672px;
    width: 230px;
    text-align: right;
    font-family: "Roboto Condensed", sans-serif;
    font-style: italic;
    font-weight: 800;
    font-size: 38px;
    line-height: 46px;
    color: var(--ink);
  }
  .car-photo {
    position: absolute;
    left: 255px; top: 596px;
    width: 649px; height: 392px;
    border-radius: 120px 0 40px 160px;
    background: linear-gradient(160deg, var(--cream-car) 0%, var(--cream-car) 45%, var(--brown-car) 75%, #2a120c 100%);
  }
  .tools-art {
    position: absolute;
    left: 14px; top: 960px;
    width: 410px; height: 150px;
    background: linear-gradient(100deg, var(--mustard), #d9a92a);
    border-radius: 60px 20px 60px 10px;
    opacity: .95;
  }
  .duty {
    position: absolute;
    left: 52px; top: 1050px;
    font-family: "Roboto Condensed", sans-serif;
    font-style: italic;
    font-weight: 700;
    font-size: 24px;
    color: var(--white);
    transform: rotate(-20deg);
    transform-origin: left top;
    text-shadow: 1px 1px 0 var(--ink);
  }
  .footer-line {
    position: absolute;
    left: 0; right: 0; top: 1150px;
    text-align: center;
    font-family: "Roboto Condensed", sans-serif;
    font-style: italic;
    font-weight: 700;
    font-size: 21px;
    color: var(--navy);
    letter-spacing: .2px;
  }
</style>
</head>
<body>
<main class="cover">
  <svg class="backdrop" width="904" height="1200" viewBox="0 0 904 1200" aria-hidden="true">
    <polygon points="0,978 256,872 904,872 904,1128 0,1128" fill="var(--brick)"/>
    <polygon points="0,958 256,860 256,880 0,986" fill="var(--mustard)"/>
    <polygon points="0,954 256,856 256,862 0,960" fill="var(--ink)"/>
    <rect x="38" y="1128" width="866" height="7" fill="var(--ink)"/>
    <rect x="0" y="1135" width="904" height="65" fill="var(--white)"/>
  </svg>

  <span class="est est--label">ESTD</span>
  <span class="est est--year">1981</span>

  <h1 class="masthead masthead--first">Chrome</h1>
  <p class="masthead masthead--second">Ember</p>

  <div class="flags" role="img" aria-label="Crossed chequered racing flags"></div>

  <svg class="ribbon" viewBox="0 0 820 170" aria-hidden="true">
    <path d="M120,70 C330,40 520,0 680,10 L650,80 L805,55 L720,95 L805,120 C700,125 610,140 545,160 C520,150 540,130 560,110 C400,130 240,140 130,150 Z" fill="var(--ink)"/>
    <path d="M126,64 C330,35 520,-4 676,4 L646,74 L800,48 L712,90 L800,114 C700,118 610,132 548,152 C524,142 544,124 562,104 C400,124 240,134 132,144 Z" fill="var(--mustard)"/>
  </svg>
  <p class="ribbon-text">WE CAN FIX ANYTHING</p>

  <svg class="burst" viewBox="0 0 260 250" aria-hidden="true">
    <polygon transform="translate(-8,6)" fill="var(--ink)" points="130,10 150,60 195,30 190,85 250,85 205,120 250,160 190,165 200,225 150,195 130,245 110,195 60,225 70,165 10,160 55,120 10,85 70,85 65,30 110,60"/>
    <polygon fill="var(--brick)" points="130,10 150,60 195,30 190,85 250,85 205,120 250,160 190,165 200,225 150,195 130,245 110,195 60,225 70,165 10,160 55,120 10,85 70,85 65,30 110,60"/>
  </svg>
  <p class="burst-text">SERVICE<br>&amp;<br>REPAIR</p>

  <p class="tagline">We Make Any Model Foreign &amp; Domestic</p>

  <div class="car-photo" role="img" aria-label="Photograph of a 1930s cream and dark brown vintage sedan with whitewall tyres and red wire wheels"></div>

  <div class="tools-art" role="img" aria-label="Illustration of a yellow wrench, screwdriver and hex nuts"></div>
  <p class="duty">Mechanic on Duty</p>

  <p class="footer-line">LOREM IPSUM . DOLOR SIT AMET . CONSECTETUER ADIPISCING ELIT</p>
</main>
</body>
</html>
```